IT Consultancy Needs Daring Webpage (uncoded)

We are looking for a web page for a small IT firm, Fable Systems. We provide remote IT services, website development and IT consultancy. We are looking for a website that is a bit unique and will look both professional and cutting edge.

We are mainly targeting high cash flow small businesses.
Feel free to play with our yellow/blue theme. We where aiming for similar colours to movie posters i.e the Copper Horizon, http://lnk.vexomo.com/q3TzW. Think metallic, flashy and classy like a colourful Zumo.
Updates

We have a website but it is very poor and we would prefer if you did not use it for inspiration.

We quite like this design http://gallery.pixelorva.com/designs/web/?order=24&offset=24#/k7m9px2

The three cornerstones of our business are Consult, Support and E-Marketing

other designs are welcome as well (different from the the link above)

Target Market(s)

Small Businesses

Industry/Entity Type

Movie

Requirements
Must have
• Space for Home, Services, Contact and Blog menu bars.

Our logo is ok, you are welcome to adjust it a little to meet your needs.

While we appreciate most websites have a dense middle ground for navigation panels, we would like the most important buttons highlighted as well as a slightly interesting background for example, instead of a plain colour background, a slight hint of a pattern or image.
Should not have
• Should not have a banner.

```html
<!DOCTYPE html>
<html lang="en">
<head>
<meta charset="utf-8">
<title>Fable Systems</title>
<link rel="stylesheet" href="https://fonts.googleapis.com/css2?family=Roboto+Slab:wght@800&family=Source+Sans+3:wght@400;600;700&family=Arimo:wght@400;700&display=swap">
<style>
:root{
  --sun-light:#fff3b0;
  --sun:#f8d860;
  --sun-deep:#f0c040;
  --sky:#2aa0e6;
  --sky-deep:#1479c4;
  --sky-pale:#9dd6f6;
  --card-yellow:#ffe12e;
  --card-orange:#ffb400;
  --ink:#111111;
  --footer:#000000;
  --footer-blue:#2aa4ee;
  --tweet-orange:#f5a300;
  --white:#ffffff;
}
*{margin:0;padding:0;box-sizing:border-box}
html,body{width:1200px;height:836px;overflow:hidden}
body{position:relative;background:var(--sky);font-family:"Arimo",Arial,sans-serif;color:var(--ink)}
.site-header{position:absolute;left:0;top:0;width:1200px;height:254px;
  background:radial-gradient(ellipse at 20% 30%,var(--sun-light),var(--sun) 55%,var(--sun-deep))}
.brand{position:absolute;left:41px;top:23px;display:flex;align-items:center;gap:32px}
.brand-mark{width:170px;height:153px;border-radius:50%;background:var(--ink);border:5px solid var(--sky)}
.brand-name{font-family:"Roboto Slab",Georgia,serif;font-weight:800;font-size:52px;color:var(--ink)}
.social{position:absolute;top:18px;width:46px;height:46px;border-radius:6px;background:var(--sky-deep)}
.social-a{left:1008px}.social-b{left:1076px}
.help-button{position:absolute;left:949px;top:77px;width:237px;height:43px;border-radius:22px;
  background:linear-gradient(#6cc4f6,var(--sky-deep));border:2px solid var(--white);
  color:var(--white);font:700 20px "Arimo",Arial,sans-serif;text-align:center;line-height:39px}
.phone{position:absolute;left:970px;top:133px;font:400 27px "Arimo",Arial,sans-serif;letter-spacing:1px}
.main-nav{position:absolute;left:0;top:203px}
.main-nav svg{display:block}
.nav-links{position:absolute;left:0;top:0;height:51px;display:flex;align-items:center;
  font:400 19px "Source Sans 3",Arial,sans-serif;color:var(--ink)}
.nav-links a{color:inherit;text-decoration:none;position:absolute;white-space:nowrap}
.services-area{position:absolute;left:0;top:254px;width:1200px;height:446px;
  background:linear-gradient(#a8d8f4,var(--sky) 55%,var(--sky-deep))}
.card{position:absolute;top:279px;width:368px;height:397px;
  background:linear-gradient(var(--card-yellow),var(--card-orange));border:1px solid #f0a000}
.card-support{background:linear-gradient(var(--sky-pale),#3fb0ee);border-color:#7fcaf2}
.card h2{position:absolute;left:11px;top:14px;font:700 28px "Arimo",Arial,sans-serif}
.card-photo{position:absolute;left:9px;top:59px;width:344px;height:165px;border:1px solid var(--ink)}
.card p{position:absolute;left:15px;top:234px;width:336px;font-size:13px;line-height:19px}
.read-more{position:absolute;display:block;width:98px;height:24px;border-radius:5px;
  background:linear-gradient(#444,#111);color:var(--white);font:700 13px "Arimo",Arial,sans-serif;
  line-height:24px;padding-left:9px;text-decoration:none}
.read-more::after{content:"";position:absolute;right:9px;top:8px;border-left:5px solid var(--white);border-top:4px solid transparent;border-bottom:4px solid transparent}
.card .read-more{left:15px;top:353px}
.site-footer{position:absolute;left:0;top:700px;width:1200px;height:136px;background:var(--footer);
  border-top:2px solid var(--sky-deep);color:var(--white)}
.footer-title{position:absolute;left:13px;top:31px;font:400 19px "Arimo",Arial,sans-serif;color:var(--footer-blue)}
.footer-line{position:absolute;left:13px;font:700 13px "Arimo",Arial,sans-serif}
.footer-line span{color:var(--footer-blue)}
.footer-legal{position:absolute;left:13px;top:105px;font-size:12px}
.posts-icon{position:absolute;left:831px;top:14px;width:48px;height:48px;border-radius:6px;background:#5ccaf0}
.posts-title{position:absolute;left:891px;top:14px;font:400 19px "Arimo",Arial,sans-serif;color:var(--footer-blue)}
.posts-text{position:absolute;left:893px;top:42px;width:290px;font-size:12px;line-height:17px;color:var(--tweet-orange)}
.site-footer .read-more{left:893px;top:90px;background:linear-gradient(#666,#333)}
</style>
</head>
<body>
<header class="site-header">
  <div class="brand"><span class="brand-mark"></span><span class="brand-name">Fable Systems</span></div>
  <span class="social social-a"></span><span class="social social-b"></span>
  <a class="help-button">CAN WE HELP YOU?</a>
  <div class="phone">0400 612 378</div>
</header>
<nav class="main-nav">
  <svg width="606" height="51" viewBox="0 0 606 51"><path d="M0 0H530Q545 0 556 10L604 51H0Z" fill="#2aa0e6"/><path d="M0 2H530" stroke="#8fd2f6" stroke-width="2"/></svg>
  <div class="nav-links">
    <a style="left:20px">Home</a><a style="left:108px">I</a>
    <a style="left:156px">Services</a><a style="left:262px">I</a>
    <a style="left:307px">Blog</a><a style="left:385px">I</a>
    <a style="left:430px">Contact</a>
  </div>
</nav>
<main class="services-area"></main>
<section class="card" style="left:13px">
  <h2>CONSULT</h2>
  <div class="card-photo" role="img" aria-label="Photo of consultants meeting around an office desk" style="background:linear-gradient(135deg,#d8d4d0,#8a93a4)"></div>
  <p>Lorem ipsum dolor sit amet, consectetur adipiscing elit. Aliquam mauris nulla, interdum sit amet tristique vitae, tristique vel sapien. Ut hendrerit mollis molestie. Donec a lectus tellus. Proin justo diam, semper et consectetur eu, consectetur ac velit. Curabitur viverra mollis lacus, et</p>
  <a class="read-more">read more</a>
</section>
<section class="card card-support" style="left:418px">
  <h2>SUPPORT</h2>
  <div class="card-photo" role="img" aria-label="Photo of a support worker at a computer desk" style="background:linear-gradient(135deg,#f0eeee,#c44a5a 60%,#7a8088)"></div>
  <p>Lorem ipsum dolor sit amet, consectetur adipiscing elit. Aliquam mauris nulla, interdum sit amet tristique vitae, tristique vel sapien. Ut hendrerit mollis molestie. Donec a lectus tellus. Proin justo diam, semper et consectetur eu, consectetur ac velit. Curabitur viverra mollis lacus, et</p>
  <a class="read-more">read more</a>
</section>
<section class="card" style="left:822px">
  <h2>E MARKETING</h2>
  <div class="card-photo" role="img" aria-label="Illustration of a large metallic at sign on blue" style="background:linear-gradient(135deg,#0c2a5a,#3a78c0 55%,#9aa8b8)"></div>
  <p>Lorem ipsum dolor sit amet, consectetur adipiscing elit. Aliquam mauris nulla, interdum sit amet tristique vitae, tristique vel sapien. Ut hendrerit mollis molestie. Donec a lectus tellus. Proin justo diam, semper et consectetur eu, consectetur ac velit. Curabitur viverra mollis lacus, et</p>
  <a class="read-more">read more</a>
</section>
<footer class="site-footer">
  <div class="footer-title">FABLE SYSTEMS</div>
  <div class="footer-line" style="top:62px"><span>Tel :</span> +0400 612 378</div>
  <div class="footer-line" style="top:80px"><span>Office Hours :</span> 9.00 am till 5.30 pm</div>
  <div class="footer-legal">Privacy Policy &nbsp;&nbsp;|&nbsp;&nbsp; Sitemap &nbsp;&nbsp;&nbsp;&nbsp;|&nbsp;&nbsp;&nbsp;&nbsp; © 2011 fablesystems.net | All rights reserved</div>
  <span class="posts-icon"></span>
  <div class="posts-title">Latest Posts</div>
  <p class="posts-text">Lorem ipsum dolor sit amet, consectetur adipiscing elit. Aliquam mauris nulla, interdum sit amet</p>
  <a class="read-more">read more</a>
</footer>
</body>
</html>
```